Margarita Company needs Table Tent Design

Ever at a restaurant and see a mouth-watering table side advertisement for a refreshing beverage? We make Margarita Mix. We need to design a Table Tent for display on the tables in Mexican restaurants to encourage restaurant patrons to order more Copper Lantern Margaritas. Design is 2 sided - each side is 4.5" (wide) x 6" (tall).

Target Market(s)

Restaurant Patrons that are visiting a restaurant, generally Mexican restaurants.

Industry/Entity Type

Mexican Restaurant

Font styles to use
Serif

Requirements
Must have
• Mouth-watering design.
Nice to have
• Marketing copy that sells more drinks.
Should not have
• Inappropriate language or images that you wouldn't share with a parent. Also, our main goal is to help the restaurants sell more drinks so we do not usually feature our company logo but we like to add our company web address in a subtle manner.

```html
<!DOCTYPE html>
<html lang="en">
<head>
<meta charset="utf-8">
<title>Copper Lantern Margaritas – Table Tent</title>
<link href="https://fonts.googleapis.com/css2?family=Bebas+Neue&family=Great+Vibes&family=Parisienne&family=Open+Sans:wght@400&display=swap" rel="stylesheet">
<style>
  :root {
    --stage: #dededc;
    --panel-black: #0b0b0d;
    --panel-navy: #0d1230;
    --ink-white: #ffffff;
    --ink-soft: #e6e6e6;
    --rule: rgba(255,255,255,0.85);
    --glass-pale: #c9d6d8;
    --glass-shade: #5d6a70;
    --citrus: #f0b431;
    --citrus-deep: #c9781f;
  }
  * { box-sizing: border-box; margin: 0; padding: 0; }
  html, body { width: 1200px; height: 739px; overflow: hidden; }
  body { background: var(--stage); position: relative; font-family: "Open Sans", sans-serif; }

  .tent-side {
    position: absolute;
    top: 60px;
    width: 465px;
    height: 620px;
    overflow: hidden;
  }
  .tent-side--front { left: 105px; background: var(--panel-black); }
  .tent-side--back {
    left: 630px;
    background: linear-gradient(160deg, #070812 0%, var(--panel-navy) 55%, #142a66 100%);
  }

  .frame {
    position: absolute;
    border: 1.5px solid var(--rule);
  }
  .tent-side--front .frame { left: 40px; top: 95px; width: 370px; height: 490px; }
  .tent-side--back .frame { left: 40px; top: 300px; width: 390px; height: 290px; }

  .photo { position: absolute; }
  .photo--white-margarita {
    left: 200px; top: 170px; width: 265px; height: 450px;
    background: linear-gradient(100deg, rgba(11,11,13,0) 0%, rgba(93,106,112,0.55) 30%, var(--glass-pale) 60%, var(--glass-shade) 100%);
  }
  .photo--bar-lights {
    left: 230px; top: 30px; width: 235px; height: 250px;
    background: radial-gradient(ellipse at 65% 55%, rgba(150,70,90,0.35) 0%, rgba(13,18,48,0) 70%);
  }
  .photo--gold-margarita {
    left: 220px; top: 330px; width: 245px; height: 290px;
    background: linear-gradient(100deg, rgba(13,18,48,0) 0%, rgba(201,120,31,0.55) 30%, var(--citrus) 65%, var(--citrus-deep) 100%);
  }

  .headline {
    position: absolute;
    left: 28px; top: 22px;
    padding-right: 8px;
    font-family: "Bebas Neue", sans-serif;
    font-size: 128px;
    line-height: 1;
    letter-spacing: 1px;
    color: var(--ink-white);
    background: var(--panel-black);
  }

  .product-name {
    position: absolute;
    font-family: "Great Vibes", cursive;
    color: var(--ink-white);
    line-height: 1.05;
  }
  .tent-side--front .product-name { left: 62px; top: 390px; font-size: 40px; }
  .tent-side--back .product-name { left: 58px; top: 400px; font-size: 36px; }

  .price-list {
    position: absolute;
    left: 48px; top: 38px;
    width: 375px;
    list-style: none;
  }
  .price-list__item {
    display: flex;
    align-items: baseline;
    height: 36px;
    font-family: "Parisienne", cursive;
    color: var(--ink-soft);
    font-size: 17px;
  }
  .price-list__leader {
    flex: 1;
    border-bottom: 1px dashed rgba(255,255,255,0.6);
    margin: 0 8px;
    transform: translateY(-4px);
  }
  .price-list__price { font-size: 18px; }

  .web-address {
    position: absolute;
    left: 58px; top: 548px;
    font-size: 13px;
    color: var(--ink-soft);
    letter-spacing: 0.5px;
  }
</style>
</head>
<body>
  <section class="tent-side tent-side--front" aria-label="Table tent front side">
    <div class="photo photo--white-margarita" role="img" aria-label="Photo of a salt-rimmed white margarita with a lemon slice and a splash at its base"></div>
    <div class="frame"></div>
    <h1 class="headline">TODAY’S</h1>
    <p class="product-name">Copper Lantern<br>Margaritas<br>Blend</p>
  </section>

  <section class="tent-side tent-side--back" aria-label="Table tent back side">
    <div class="photo photo--bar-lights" role="img" aria-label="Soft blurred bar lights behind rain drops"></div>
    <ul class="price-list">
      <li class="price-list__item"><span>Classic Lime</span><span class="price-list__leader"></span><span class="price-list__price">209</span></li>
      <li class="price-list__item"><span>Frozen Mango</span><span class="price-list__leader"></span><span class="price-list__price">209</span></li>
      <li class="price-list__item"><span>Spicy Jalapeño</span><span class="price-list__leader"></span><span class="price-list__price">209</span></li>
      <li class="price-list__item"><span>Strawberry Swirl</span><span class="price-list__leader"></span><span class="price-list__price">209</span></li>
      <li class="price-list__item"><span>Golden Cadillac</span><span class="price-list__leader"></span><span class="price-list__price">209</span></li>
      <li class="price-list__item"><span>Blood Orange</span><span class="price-list__leader"></span><span class="price-list__price">209</span></li>
    </ul>
    <div class="photo photo--gold-margarita" role="img" aria-label="Photo of a golden margarita with a salted rim and a lime slice"></div>
    <div class="frame"></div>
    <p class="product-name">Copper Lantern<br>Margaritas<br>Blend</p>
    <p class="web-address">www.copperlanternmix.com</p>
  </section>
</body>
</html>
```